ReDesign of Veltrano.info and Veltrano app

Veltrano:

Veltrano aims to be your own personal cloud of profile information with ability to share a part of it with others based on the consumer.

As we visit different sites and buy different products, apply for new jobs, on-board in a company or fill out a basic form at a doctors office, we end up entering the same information again and again albeit with some sections different based on where you are. For example, we enter some basic informaiton “AND” billing address on brindle, vs you enter some basic information “AND” work history on a job site.

What if you created a profile one time and then create justed avatars or keys to a combination of information and at different places use different keys to unlock that specific piece of information.

Use Case 1: Marek Dunhill applying for a job
Marek goes to hire trellis, creates new login, enters where he lives, email, phone, then goes into the most tedious phase of entering work history. He realizes, he also needs to go to Quarnel.com and do the exact same thing and so on on any job site he visits in future.

With Veltrano
Marek goes to Veltrano, updates all his work history, personal information (No SSN or credit card). Now he creates a new “key” called “mareksjobapplication” with a cryptic “keycode” and chooses to share personal information + work history for this key. He now goes to any job site to see a “VT” icon. He clicks on that, a pop-up box with key and keycode appears. He ONLY enters mareksjobapplicaiton and the keycode he had set, boom, all his work informaiton is auto-populated in hire trellis. Immense savings in time for Marek.

Use Case 2: Sharing contact information
Marek meets a beautiful at a bar and thinks he needs to share his personal information but only has a 5 mintue window. He realizes, he has created a key named “Marek007” and has chosen to share his personal information only (no work information). She asks for contact number, he gives her is VT key. She pulls up VT app instead of contact list to add contact, plugs in Marek007 (and a key if marek decides to protect this key with a code) and boom, she has mareks phone/email/picture (yes picture), chatterloop blog and a contact is automatically created!!!!! She now can really associate this Marek from 8 other Marek’s in the bar!!

Use Case 3: Always stay connected
Marek is bored of Houston and decides to move to LA.He wants a local phone number for people to get in touch with them easily. But now he has to do the painful job of sending all his friends his updated number/contact address. If he had exchanged information with Veltrano key with his friends, his contact information with them is always in sync. TThe Veltrano app is intelligent to know that new information is available for the same profile key. As long as the passcode is the same, that information is automatically updated in the consumers contact list. Next time Marek’s friend picks up the phone, he just need so hit “DIAL”. The correct number is dialed. Along with that, his friends now also have his updated address information which he had shared with the key.

SECURITY
Anytime anyone views your profile using your profile key, you automatically get notified to your registered email address of someone pulling up your profile. If you think it’s suspicious, you can change the access code or set an access code to that public key.

where to go:
Go to http://veltrano.info
Register and play around with different views you can create for your profile with different access codes

Download
Veltrano app from pomelo appmart or Zentrix playmart. We need a nice look and feel for the app as well.

Target Market(s)

students, careers, hiring companies, anyone starting online presence

Industry/Entity Type

Credit Card

Requirements
Must have

• convey message, simplistic, an app to consume data, always stay updated with friends emails etc
Nice to have
• logo should show a user and multiple facets of user for multiple consumers

```html
<!DOCTYPE html>
<html lang="en">
<head>
<meta charset="utf-8">
<title>Veltrano – Your single Online Contact Card</title>
<link rel="stylesheet" href="https://fonts.googleapis.com/css2?family=Ubuntu:ital,wght@0,300;0,400;0,500;1,400&display=swap">
<style>
  :root {
    --ink: #3f4a50;
    --ink-soft: #555;
    --muted: #9a9a9a;
    --nav: #4a5358;
    --accent: #2a9fe0;
    --sky-top: #cfe9f6;
    --sky-mid: #e8f5fb;
    --band: #f8f8f8;
    --rule: #e4e4e4;
    --btn-top: #cdeefb;
    --btn-bot: #86cfee;
    --btn-edge: #6fb8d8;
    --topbar-top: #f3f3f3;
    --topbar-bot: #d2d2d2;
    --art-cloud: #bfe2f3;
    --art-green: #9ccc3c;
    --art-orange: #e9a75a;
    --art-blue: #4f7fb8;
  }
  * { box-sizing: border-box; margin: 0; padding: 0; }
  html, body { width: 1200px; height: 1198px; overflow: hidden; background: #fff; }
  body { font-family: "Ubuntu", sans-serif; color: var(--ink-soft); position: relative; }

  .utility-bar {
    position: absolute; left: 0; top: 0; width: 1200px; height: 28px;
    background: linear-gradient(var(--topbar-top), var(--topbar-bot));
  }
  .utility-bar ul { position: absolute; left: 526px; top: 0; display: flex; list-style: none; height: 28px; border-left: 1px solid #c4c4c4; }
  .utility-bar li { font-size: 9px; color: #7a8a94; padding: 0 12px; line-height: 28px; border-right: 1px solid #c4c4c4; display: flex; align-items: center; gap: 5px; }
  .utility-bar li i { width: 10px; height: 9px; background: #8fb3cc; border-radius: 2px; display: inline-block; }

  .brand { position: absolute; left: 224px; top: 74px; display: flex; align-items: center; gap: 10px; }
  .brand-dot { width: 30px; height: 30px; border-radius: 50%; background: #9fd6f0; }
  .brand-name { font-size: 28px; font-weight: 300; color: var(--ink); }

  .main-nav { position: absolute; top: 63px; left: 582px; display: flex; list-style: none; }
  .main-nav li { font-size: 11px; color: var(--nav); padding: 0 9px; line-height: 19px; }
  .main-nav li.active { background: var(--accent); color: #fff; }

  .hero {
    position: absolute; left: 0; top: 157px; width: 1200px; height: 511px;
    background: linear-gradient(180deg, var(--sky-top) 0%, var(--sky-mid) 55%, #fff 100%);
  }
  .hero-title { position: absolute; left: 221px; top: 252px; font-size: 52px; font-weight: 300; color: var(--ink); letter-spacing: -0.5px; }
  .hero-sub { position: absolute; left: 224px; top: 312px; font-size: 17px; color: var(--ink); }
  .hero-copy { position: absolute; left: 224px; top: 340px; width: 280px; font-size: 10.5px; line-height: 17.5px; color: var(--ink); }
  .btn {
    display: block; text-align: center; color: var(--ink);
    background: linear-gradient(var(--btn-top), var(--btn-bot));
    border: 1px solid var(--btn-edge); border-radius: 2px;
    box-shadow: 0 2px 3px rgba(0,0,0,.18);
  }
  .hero-cta { position: absolute; left: 223px; top: 400px; width: 233px; height: 37px; line-height: 35px; font-size: 16px; }

  .hero-art {
    position: absolute; left: 540px; top: 100px; width: 600px; height: 560px;
    border-radius: 28px;
    background:
      radial-gradient(ellipse 130px 95px at 24% 76%, var(--art-cloud) 0%, var(--art-cloud) 70%, rgba(191,226,243,0) 100%),
      radial-gradient(ellipse 110px 130px at 55% 78%, rgba(233,167,90,.85) 0%, rgba(233,167,90,.55) 55%, rgba(233,167,90,0) 100%),
      radial-gradient(ellipse 150px 230px at 52% 42%, rgba(156,204,60,.55) 0%, rgba(156,204,60,.2) 60%, rgba(156,204,60,0) 100%),
      radial-gradient(ellipse 180px 260px at 82% 38%, rgba(79,127,184,.35) 0%, rgba(79,127,184,.12) 60%, rgba(79,127,184,0) 100%),
      linear-gradient(160deg, rgba(255,255,255,.55), rgba(214,236,248,.75));
  }

  .testimonial {
    position: absolute; left: 0; top: 668px; width: 1200px; height: 125px;
    background: var(--band); border-top: 1px solid var(--rule); border-bottom: 1px solid var(--rule);
  }
  .quote-mark { position: absolute; font-size: 150px; font-family: Georgia, serif; color: #c4c4c4; line-height: 1; font-weight: 700; }
  .quote-mark.open { left: 134px; top: -22px; }
  .quote-mark.close { left: 985px; top: 20px; }
  .testimonial h2 { position: absolute; left: 223px; top: 22px; font-size: 17px; font-weight: 300; color: var(--ink); }
  .testimonial p { position: absolute; left: 223px; top: 42px; width: 750px; font-size: 10.5px; line-height: 16px; color: var(--ink-soft); }
  .testimonial cite { position: absolute; left: 765px; top: 83px; font-size: 11.5px; font-style: italic; color: #666; }
  .testimonial .role { position: absolute; left: 765px; top: 101px; font-size: 10px; font-style: italic; color: #666; }

  .features { position: absolute; left: 224px; top: 845px; display: flex; gap: 15px; }
  .feature { width: 240px; text-align: center; }
  .feature-photo { width: 240px; height: 146px; border-radius: 70px 70px 40px 40px; }
  .feature h3 { margin-top: 18px; font-size: 24px; font-weight: 300; color: var(--ink); }
  .feature .tagline { margin-top: 0; font-size: 14px; font-weight: 300; color: var(--muted); padding-bottom: 9px; border-bottom: 1px solid #cfcfcf; }
  .feature p { margin-top: 9px; font-size: 10.5px; line-height: 16px; color: #444; }
  .feature .btn { width: 131px; height: 26px; line-height: 24px; font-size: 11px; margin: 16px auto 0; }
</style>
</head>
<body>
  <nav class="utility-bar" aria-label="Quick links">
    <ul>
      <li><i></i>Live Chat Online Now</li>
      <li><i></i>Support</li>
      <li><i></i>Email</li>
      <li><i></i>Sales</li>
      <li><i></i>Customer Login</li>
    </ul>
  </nav>

  <div class="brand"><span class="brand-dot"></span><span class="brand-name">Veltrano</span></div>

  <ul class="main-nav">
    <li class="active">Home</li>
    <li>About</li>
    <li>Account</li>
    <li>How it works</li>
    <li>Partner with Us</li>
    <li>Contact Us</li>
  </ul>

  <section class="hero"></section>
  <div class="hero-art" role="img" aria-label="Illustration of a profile cloud with colourful swirls and cords reaching out to contact, mail, phone and social icons"></div>
  <h1 class="hero-title">Veltrano</h1>
  <p class="hero-sub">Your single Online Contact Card</p>
  <p class="hero-copy">This is Photoshop's version of Lorem Ipsum. Proin gravida nibh vel velit auctor aliquet. Aenean sollicitudin, lorem quis bibendum auctor, nisi elit consequat</p>
  <a class="btn hero-cta">Create your free Veltrano</a>

  <section class="testimonial">
    <span class="quote-mark open">“</span>
    <span class="quote-mark close">”</span>
    <h2>Networking is now much more Fun !!</h2>
    <p>Lorem Ipsum. Proin gravida nibh vel velit auctor aliquet. Aenean sollicitudin, lorem quis bibendum auctor, nisi elit consequat ipsum, nec sagittis sem nibh id elit. Duis sed odio sit amet nibh vulputate cursus a sit amet mauris. Morbi accumsan ipsum velit. Nam nec tellus a odio tincidunt auctor a ornare odio. Sed non mauris vitae erat consequat auctor eu in elit.</p>
    <cite>Dov Kessler</cite>
    <span class="role">Founder and CEO, Northbay Sound Network</span>
  </section>

  <section class="features">
    <article class="feature">
      <div class="feature-photo" role="img" aria-label="Photo of a person speaking into a headset microphone" style="background:linear-gradient(120deg,#b77b4a,#e2b48a 55%,#e8e8e8)"></div>
      <h3>Personal Cloud</h3>
      <div class="tagline">of your profile information</div>
      <p>Lorem velit auctor aliquet. Aenean sollicitudin, lorem quis bibendum auctor, nisi elit consequat ipsum, nec sagittis sem nibh id elit.</p>
      <a class="btn">Get Started</a>
    </article>
    <article class="feature">
      <div class="feature-photo" role="img" aria-label="Photo of sliced watermelon" style="background:linear-gradient(120deg,#c8262e,#e0484a 50%,#4f7a32)"></div>
      <h3>Update Everyone</h3>
      <div class="tagline">sync all your contact cards</div>
      <p>Lorem velit auctor aliquet. Aenean sollicitudin, lorem quis bibendum auctor, nisi elit consequat ipsum, nec sagittis sem nibh id elit.</p>
      <a class="btn">Get Started</a>
    </article>
    <article class="feature">
      <div class="feature-photo" role="img" aria-label="Photo of a young man in a hooded top on a dark blue background" style="background:linear-gradient(120deg,#1c3558,#2d4a70 50%,#6b6a66)"></div>
      <h3>Multiple Avatars</h3>
      <div class="tagline">different profile info keys</div>
      <p>Lorem velit auctor aliquet. Aenean sollicitudin, lorem quis bibendum auctor, nisi elit consequat ipsum, nec sagittis sem nibh id elit.</p>
      <a class="btn">Get Started</a>
    </article>
  </section>
</body>
</html>
```